Poster / Flyer / Advertisement for Frostel Brew Chips (Unique Product!)

We’re selling alcoholic (7.5%) flavored ice for beer…for example, you might try our Lime flavor in a Velmora. We need a great ad/poster…please follow these guidelines:
USE THE PRODUCT PHOTO & KEEP IT SIMPLE!
Use the attached “action shot” of our product prominently. I prefer just the glass of beer, so turn off the layer with the beer bottle. Photoshop in a great background and KEEP IT SIMPLE - the product shot pretty much says it all. Find a great background, add the words “Your beer is getting warm”, and layer in some of our branding (see below). That’s it! Don’t make the poster too busy!
USE OUR CURRENT BRANDING
I’ve attached AI files with all of our branding. Layer in the pattern used on the packaging, our logo, and probably the “Frostel Chill” banner. Also, given that our most popular flavor is Lime in a Velmora, I would look for a background that helps express that (just a thought, it’s up to you to make it look good!).
MAKE IT VERSATILE
We need this to be versatile and easily scale up or down in size for various applications such as:
1) Large format poster for the front window of a convenience store
2) Smaller format for poster ads in bars/restaurants
3) Even smaller format for window clings that go on the glass doors of beer coolers
I also want the words for the poster to be easily changeable for the different applications:
1) Bar – I would use the tagline “Your beer is getting warm”
2) Convenience Store – I would use the line “Don’t drink warm beer…check the freezer!” or something similar. Just need it easy to change
Updates
Reason: Still deciding on designs. Need time to review with business partners. Thanks all!
Target Market(s)
Beer drinkers - especially those that like fruity beers like summer shandy
Industry/Entity Type
Brewery
Font styles to use
Other font styles liked:
- Use attached fonts!
Colors
Designer to choose colors to be used in the design.
Requirements
Must have
- Use the product shot and our branding...and a simple design!
Nice to have
- Want a "drinking an ice cold beer on a summer day" feel to this.

```html
<!DOCTYPE html>
<html lang="en">
<head>
<meta charset="utf-8">
<title>Frostel Brew Chips – Your Beer Is Getting Warm</title>
<link rel="stylesheet" href="https://fonts.googleapis.com/css2?family=Jost:wght@600;700;800&display=swap">
<style>
  :root {
    --page-bg: #f1f1f1;
    --sun-core: #ffe64d;
    --sun-edge: #ffd400;
    --ink: #1f1d1a;
    --band: #231f1c;
    --lime: #8fd14f;
    --glass-top: #f6f0c8;
    --glass-mid: #f3dc5c;
    --glass-low: #f6ebb0;
  }
  * { box-sizing: border-box; margin: 0; padding: 0; }
  html, body {
    width: 1200px;
    height: 1200px;
    overflow: hidden;
    background: var(--page-bg);
    font-family: "Jost", "Futura", sans-serif;
  }
  .poster {
    position: absolute;
    left: 220px;
    top: 30px;
    width: 760px;
    height: 1140px;
    overflow: hidden;
    background: radial-gradient(circle at 50% 52%, var(--sun-core) 0%, var(--sun-edge) 70%);
  }
  .product-shot {
    position: absolute;
    left: 270px;
    top: 176px;
    width: 211px;
    height: 440px;
    border-radius: 6px 6px 14px 14px;
    background: linear-gradient(180deg, var(--glass-top) 0%, var(--glass-top) 24%, var(--glass-mid) 45%, var(--glass-mid) 78%, var(--glass-low) 100%);
    clip-path: polygon(4% 20%, 96% 20%, 90% 100%, 10% 100%);
  }
  .headline {
    position: absolute;
    left: 0;
    width: 100%;
    top: 640px;
    text-align: center;
    color: var(--ink);
    font-weight: 700;
    text-transform: uppercase;
    line-height: 1;
  }
  .headline .line { display: block; font-size: 55px; letter-spacing: 0.5px; margin-bottom: 8px; }
  .headline .line--big { font-size: 94px; font-weight: 800; letter-spacing: 1px; margin-top: -2px; }
  .steps-band {
    position: absolute;
    left: 0;
    top: 998px;
    width: 545px;
    height: 77px;
    background: var(--band);
    border-radius: 0 40px 40px 0 / 0 80px 80px 0;
    display: flex;
    align-items: center;
    padding-left: 58px;
    color: var(--lime);
    font-weight: 700;
    font-size: 23px;
    letter-spacing: 0.5px;
  }
  .step { display: flex; align-items: center; gap: 12px; }
  .step svg { width: 34px; height: 34px; }
  .step-divider { width: 2px; height: 38px; background: var(--lime); margin: 0 20px; }
  .brand-mark {
    position: absolute;
    left: 578px;
    top: 981px;
    width: 134px;
    height: 134px;
    border-radius: 50%;
    background: var(--band);
    display: flex;
    align-items: center;
    justify-content: center;
    text-align: center;
  }
  .brand-name {
    color: var(--lime);
    font-weight: 700;
    font-size: 17px;
    line-height: 1.15;
    text-transform: uppercase;
    letter-spacing: 1px;
  }
</style>
</head>
<body>
  <main class="poster">
    <div class="product-shot" role="img" aria-label="Pint glass of cold lager with a lime-flavoured ice chip splashing into it"></div>

    <h1 class="headline">
      <span class="line">Your beer</span>
      <span class="line">is getting</span>
      <span class="line line--big">Warm</span>
    </h1>

    <div class="steps-band">
      <div class="step">
        <svg viewBox="0 0 34 34" aria-hidden="true" fill="none" stroke="currentColor" stroke-width="3" stroke-linecap="round">
          <line x1="17" y1="3" x2="17" y2="31"/>
          <line x1="5" y1="10" x2="29" y2="24"/>
          <line x1="5" y1="24" x2="29" y2="10"/>
        </svg>
        <span>Freeze</span>
      </div>
      <span class="step-divider"></span>
      <div class="step">
        <svg viewBox="0 0 34 34" aria-hidden="true" fill="none" stroke="currentColor" stroke-width="2.5" stroke-linejoin="round">
          <line x1="14" y1="2" x2="14" y2="9"/>
          <line x1="19" y1="2" x2="19" y2="9"/>
          <rect x="8" y="14" width="18" height="16" rx="3"/>
        </svg>
        <span>Drop</span>
      </div>
      <span class="step-divider"></span>
      <div class="step">
        <svg viewBox="0 0 34 34" aria-hidden="true" fill="none" stroke="currentColor" stroke-width="2.5" stroke-linejoin="round">
          <rect x="6" y="8" width="17" height="22" rx="2"/>
          <path d="M23 13h4a3 3 0 0 1 3 3v5a3 3 0 0 1-3 3h-4"/>
          <path d="M5 9c0-4 4-5 6-4 1-2 6-2 7 0 2-1 6 0 6 4"/>
        </svg>
        <span>Enjoy</span>
      </div>
    </div>

    <div class="brand-mark">
      <span class="brand-name">Frostel<br>Brew<br>Chips</span>
    </div>
  </main>
</body>
</html>
```